Cleaning Company needs a new business card design

Hi, We are looking for new business card designs to update with our latest logo and company information.
We would like to see designs using the colours:
Royal Blue #4169E1 - this is our company colour so this has to be in there. Please feel free to experiment with other colours.
Must include:
Front of business card:
Logo
Back of the business card:
0800 529 6081
07438 915 702
Email: info@pkrtidyhomes.co.uk
Web: www.pkrtidyhomes.co.uk
Services:
End of Tenancy
Carpet & Upholstery
Regular & One Off
all work fully insured.
The front of the business card with the logo can be made to look raised print. The blue man to be a shiny finish.
The business card needs to be presented in a matt finish
The business must be in the following styles:
Standard Square with rounded corners.
Thank you to all that take part in this.
Target Market(s)
Men and Women of different ages in the UK.
Industry/Entity Type
House Cleaning
Contact Information for Business Card
Front of business card:
Logo
0800 529 6081
07438 915 702
Email: pkrtidy@mailbox-demo.co.uk
Services:
End of Tenancy
Carpet & Upholstery
Regular & One Off
all work fully insured.

```html
<!DOCTYPE html>
<html lang="en">
<head>
<meta charset="utf-8">
<title>PKR Tidy Homes Limited – Business Card</title>
<link rel="stylesheet" href="https://fonts.googleapis.com/css2?family=Questrial&family=Jost:ital,wght@0,400;0,500;1,500;1,700&display=swap">
<style>
  :root {
    --card-blue: #2b47a8;
    --royal-blue: #4169E1;
    --accent-cyan: #35a9e6;
    --paper: #ffffff;
    --ink: #1f1f24;
    --muted: #8a8a90;
    --backdrop-light: #e4e4e6;
    --backdrop-dark: #8c8c90;
  }
  * { box-sizing: border-box; margin: 0; padding: 0; }
  html, body { width: 1200px; height: 960px; overflow: hidden; }
  body {
    background: radial-gradient(ellipse at 40% 40%, var(--backdrop-light) 0%, #c4c4c7 55%, var(--backdrop-dark) 100%);
    position: relative;
    font-family: "Jost", sans-serif;
  }
  .card {
    position: absolute;
    width: 520px;
    height: 320px;
    border-radius: 22px;
    overflow: hidden;
    box-shadow: 0 18px 40px rgba(0,0,0,0.25);
  }
  /* Front */
  .card-front {
    left: 50px; top: 320px;
    background: linear-gradient(135deg, #2f4fb4 0%, var(--card-blue) 100%);
    display: flex; align-items: center; justify-content: center; gap: 22px;
  }
  .front-mark {
    width: 54px; height: 54px; border-radius: 50%;
    background: var(--accent-cyan);
  }
  .front-name {
    font-family: "Questrial", sans-serif;
    color: var(--paper);
    font-size: 44px;
    line-height: 1.05;
  }
  /* Back */
  .card-back {
    left: 630px; top: 320px;
    background: var(--paper);
  }
  .back-top { position: absolute; left: 0; top: 0; width: 100%; height: 140px; }
  .back-brand {
    position: absolute; left: 44px; top: 38px;
    display: flex; align-items: center; gap: 14px;
  }
  .back-mark { width: 30px; height: 30px; border-radius: 50%; background: var(--accent-cyan); }
  .back-name {
    font-family: "Questrial", sans-serif;
    color: var(--card-blue);
    font-size: 30px;
    line-height: 1.1;
  }
  .holder {
    position: absolute; right: 30px; top: 78px; text-align: right;
  }
  .holder-name { font-style: italic; font-weight: 500; font-size: 20px; color: var(--ink); }
  .holder-title { font-style: italic; font-weight: 500; font-size: 12px; color: var(--muted); margin-top: 2px; }
  .back-band {
    position: absolute; left: 0; top: 140px; width: 100%; height: 180px;
    background: var(--card-blue);
    color: var(--paper);
    display: flex; padding: 30px 26px 0 26px; gap: 30px;
  }
  .services { list-style: none; font-size: 14px; line-height: 1.5; }
  .services li::before { content: "• "; }
  .insured {
    font-style: italic; font-weight: 700; font-size: 14px; letter-spacing: 0.3px;
    margin-top: 10px; text-transform: uppercase;
  }
  .contacts { list-style: none; font-size: 15px; line-height: 1.6; }
  .contacts li { display: flex; align-items: center; gap: 8px; }
  .contacts svg { width: 15px; height: 15px; flex: none; }
</style>
</head>
<body>
  <section class="card card-front" aria-label="Card front">
    <span class="front-mark"></span>
    <span class="front-name">PKR Tidy Homes<br>Limited</span>
  </section>

  <section class="card card-back" aria-label="Card back">
    <div class="back-top">
      <div class="back-brand">
        <span class="back-mark"></span>
        <span class="back-name">PKR Tidy Homes<br>Limited</span>
      </div>
      <div class="holder">
        <div class="holder-name">First &amp; Last Name</div>
        <div class="holder-title">Title Here</div>
      </div>
    </div>
    <div class="back-band">
      <div class="service-block">
        <ul class="services">
          <li>End of Tenancy</li>
          <li>Carpet &amp; Upholstery</li>
          <li>Regular &amp; One Off</li>
        </ul>
        <p class="insured">All work fully insured</p>
      </div>
      <ul class="contacts">
        <li><svg viewBox="0 0 16 16"><circle cx="8" cy="8" r="8" fill="var(--accent-cyan)"/><path d="M5.5 4.5l1.5 0 .7 2-1 .8a5 5 0 0 0 2 2l.8-1 2 .7v1.5c0 .5-.5 1-1 1A6 6 0 0 1 4.5 5.5c0-.5.5-1 1-1z" fill="#fff"/></svg>0800 529 6081</li>
        <li><svg viewBox="0 0 16 16"><circle cx="8" cy="8" r="8" fill="var(--accent-cyan)"/><rect x="5.5" y="3.5" width="5" height="9" rx="1" fill="#fff"/></svg>07438 915 702</li>
        <li><svg viewBox="0 0 16 16"><circle cx="8" cy="8" r="8" fill="var(--accent-cyan)"/><rect x="4" y="5" width="8" height="6" fill="#fff"/><path d="M4 5l4 3 4-3" stroke="var(--accent-cyan)" fill="none"/></svg>pkrtidy@mailbox-demo.co.uk</li>
        <li><svg viewBox="0 0 16 16"><circle cx="8" cy="8" r="8" fill="var(--accent-cyan)"/><circle cx="8" cy="8" r="4" fill="none" stroke="#fff" stroke-width="1.3"/><path d="M4 8h8M8 4v8" stroke="#fff" stroke-width="1"/></svg>www.pkrtidyhomes.co.uk</li>
      </ul>
    </div>
  </section>
</body>
</html>
```